Butcher shop

We have 2 butcher shops:

Shop 9, Ridgeway Court, Aberdeen NSW 2336
Ph 02 6512 3840

47 Marlow St, Scone NSW 2337
Ph 02 6518 2274

ABN 48 907 215 816

I would like this info on reverse of card and my personal info on front of card. I have a logo I would like to use also. Require a very smooth thick matte card, with colour both sides.

Front of card should say:

Linda Farrugia
Accounts

Ph 0437 620 915
E lindafarrugia@quollmail.com.au

Industry/Entity Type

Shop

Contact Information for Business Card

Linda Farrugia
Ph 0437 620 915

Logo Text

Farrugia's Quality Meats

Logo styles of interest
Pictorial/Combination Logo
Requirements
Must have
• We use Century Gothic Font

```html
<!DOCTYPE html>
<html lang="en">
<head>
<meta charset="utf-8">
<title>Business Card – Reverse</title>
<link rel="stylesheet" href="https://fonts.googleapis.com/css2?family=Jost:wght@400&display=swap">
<style>
  :root {
    --band-blue: #84d3f0;
    --card-white: #ffffff;
    --ink: #111111;
  }
  html, body {
    margin: 0;
    padding: 0;
    overflow: hidden;
  }
  .card {
    width: 1200px;
    height: 692px;
    display: grid;
    grid-template-rows: 346px 241px 105px;
    font-family: "Jost", "Century Gothic", sans-serif;
    font-weight: 400;
    color: var(--ink);
  }
  .shop {
    display: flex;
    flex-direction: column;
    align-items: center;
    justify-content: center;
    text-align: center;
  }
  .shop--aberdeen {
    background: var(--band-blue);
    padding-top: 40px;
    box-sizing: border-box;
  }
  .shop--scone {
    background: var(--card-white);
  }
  .shop__address,
  .shop__phone {
    font-size: 47px;
    line-height: 62px;
    margin: 0;
  }
  .shop__phone {
    display: flex;
    align-items: center;
    gap: 8px;
  }
  .phone-icon {
    width: 34px;
    height: 34px;
  }
  .abn {
    background: var(--band-blue);
    display: flex;
    align-items: center;
    justify-content: center;
    font-size: 41px;
    margin: 0;
    padding-bottom: 28px;
    box-sizing: border-box;
  }
</style>
</head>
<body>
  <main class="card">
    <section class="shop shop--aberdeen">
      <p class="shop__address">Shop 9, Ridgeway Court, Aberdeen NSW 2336</p>
      <p class="shop__phone">
        <svg class="phone-icon" viewBox="0 0 34 34" aria-hidden="true">
          <circle cx="17" cy="17" r="15" fill="none" stroke="currentColor" stroke-width="2.5"/>
          <path d="M12 7 q-6 10 0 20 l5 -3 q-3 -7 0 -14 z" fill="currentColor"/>
        </svg>
        <span>02 6512 3840</span>
      </p>
    </section>
    <section class="shop shop--scone">
      <p class="shop__address">47 Marlow St, Scone NSW 2337</p>
      <p class="shop__phone">
        <svg class="phone-icon" viewBox="0 0 34 34" aria-hidden="true">
          <circle cx="17" cy="17" r="15" fill="none" stroke="currentColor" stroke-width="2.5"/>
          <path d="M12 7 q-6 10 0 20 l5 -3 q-3 -7 0 -14 z" fill="currentColor"/>
        </svg>
        <span>02 6518 2274</span>
      </p>
    </section>
    <p class="abn">ABN 48 907 215 816</p>
  </main>
</body>
</html>
```